Labels designs for a new coffee brand (Velloru Coffee)

We looking for a coffee label design for our coffee Brand, VELLORU COFFE, attached is the logo. We are bringing out to the market 3 Premium blends
1. Colombian Popayan
2. Gourmet Expresso Blend
3. Brazilian Santos

We like something that looks high quality yet modern, the bags we are using is black matte, we are starting with labels and look in the near future to print our own labels .

We want the labels for the 3 coffees to have the similar look and feel but to be uniquely identified by its design (Colombian, Brazilian, espresso) This is beig sold as a set so we want it to have a similar label feeling but that each is identify as its unique product (colombian, expresso, brazilian blend.

This project is for labels that will be used on a black matte bag, is for a 16 oz bag,

Attached is a sample of the bag color.

Size Requirements:
Maintain a 2:3 aspect ratio for the image file
The label will be 4" wide and 6" tall (we also want to print some 3X4)
Recommended image size is 1600px X 2400px

I will provide upc later

www.vellorucoffee.example pw 12345 this is the test site not live yet but you can get a feel of the brand

Ay my daughters volleyball tournament I need extra time to review

coffee drinkers

coffee

• Creativity, unique, eye catchy,

```html
<!DOCTYPE html>
<html lang="en">
<head>
<meta charset="utf-8">
<title>Velloru Coffee – Label Set</title>
<link rel="stylesheet" href="https://fonts.googleapis.com/css2?family=Quicksand:wght@500;600;700&family=Lexend:wght@500;600&display=swap">
<style>
  :root {
    --canvas: #ededed;
    --paper: #ffffff;
    --brown: #9d6545;
    --brown-band: #a26b49;
    --brown-dark: #6e4127;
    --col-yellow: #f4d600;
    --col-red: #ee4a48;
    --col-blue: #2f6fc0;
    --bra-green: #128a1a;
    --bra-yellow: #f0d200;
    --gou-tan: #d3a063;
    --gou-brown: #8a3a14;
    --gou-yellow: #f0d200;
  }
  * { margin: 0; padding: 0; box-sizing: border-box; }
  html, body { width: 1200px; height: 1200px; overflow: hidden; background: var(--canvas); }
  .label-set {
    position: relative;
    width: 1200px; height: 1200px;
    display: flex; justify-content: center; align-items: center; gap: 24px;
  }
  .label { width: 327px; height: 490px; display: block; background: var(--paper); box-shadow: 0 1px 3px rgba(0,0,0,.12); }
  .label text { font-family: "Quicksand", sans-serif; fill: var(--brown); text-anchor: middle; }
  .label .brand-name { font-weight: 700; font-size: 42px; letter-spacing: 3px; }
  .label .blend-name { font-family: "Lexend", sans-serif; font-weight: 600; font-size: 33px; letter-spacing: 1.5px; }
  .label .blend-sub { font-family: "Lexend", sans-serif; font-weight: 600; font-size: 22px; letter-spacing: 1px; }
  .label .origin { font-weight: 700; font-size: 19px; letter-spacing: 2px; }
  .label .arabica { font-weight: 700; font-size: 22px; letter-spacing: .5px; }
  .label .fresh { font-weight: 600; font-size: 15px; letter-spacing: 1px; }
  .label .scale-word { font-weight: 700; font-size: 12px; letter-spacing: 1px; }
  .label .ingredients { font-weight: 700; font-size: 17px; letter-spacing: 2px; }
  .label .roast { font-weight: 700; font-size: 15px; text-anchor: start; letter-spacing: .5px; }
  .label .weight { font-weight: 700; font-size: 12px; }
  .label .site { font-weight: 600; font-size: 15px; letter-spacing: 2.5px; fill: #fff; }
  .label .distributor { font-weight: 600; font-size: 10px; letter-spacing: .6px; fill: #fff; }
  .frame { fill: none; stroke: var(--brown); stroke-width: 6; }
  .panel { fill: var(--paper); stroke: var(--brown); stroke-width: 7; }
  .wave { fill: none; stroke: var(--brown); stroke-width: 2.5; }
  .wave-light { fill: none; stroke: #fff; stroke-width: 2.5; }
  .roast-bean { fill: var(--brown-dark); }
  .roast-bean-empty { fill: none; stroke: var(--brown-dark); stroke-width: 1.5; }
</style>
</head>
<body>
<main class="label-set">

  <!-- Colombian Popayan -->
  <svg class="label label--colombian" viewBox="0 0 526 789" role="img" aria-label="Colombian Popayan label">
    <defs>
      <linearGradient id="col-left" x1="0" y1="0" x2="0" y2="1">
        <stop offset="0" stop-color="var(--col-yellow)"/><stop offset=".45" stop-color="var(--col-blue)"/><stop offset="1" stop-color="var(--col-red)"/>
      </linearGradient>
      <linearGradient id="col-right" x1="0" y1="0" x2="0" y2="1">
        <stop offset="0" stop-color="var(--col-red)"/><stop offset=".45" stop-color="var(--col-yellow)"/><stop offset="1" stop-color="var(--col-blue)"/>
      </linearGradient>
    </defs>
    <path class="frame" d="M25 447V98A80 80 0 0 1 105 18H427A80 80 0 0 1 507 98V447"/>
    <text class="brand-name" x="263" y="234">VELLORU</text>
    <rect role="img" aria-label="scattered roasted coffee beans" x="218" y="279" width="90" height="22" rx="11" fill="var(--brown-dark)" opacity=".75"/>
    <rect role="img" aria-label="tiles of coffee beans, parrot and flowers in Colombian colours" x="0" y="467" width="90" height="233" fill="url(#col-left)"/>
    <rect role="img" aria-label="tiles of leaves, maracas and a sailboat in Colombian colours" x="437" y="465" width="89" height="235" fill="url(#col-right)"/>
    <rect x="0" y="697" width="526" height="92" fill="var(--brown-band)"/>
    <path class="panel" d="M93 697V392H128V370A34 34 0 0 1 162 336H363A34 34 0 0 1 397 370V392H434V697"/>
    <text class="blend-name" x="263" y="384">COLOMBIAN</text>
    <text class="blend-name" x="263" y="426">POPAYAN</text>
    <path class="wave" d="M157 456q4-5 8 0t8 0t8 0t8 0t8 0t8 0t8 0t8 0"/>
    <text class="origin" x="263" y="463">ORIGIN</text>
    <path class="wave" d="M308 456q4-5 8 0t8 0t8 0t8 0t8 0t8 0t8 0t8 0"/>
    <text class="arabica" x="268" y="504">100% Arabica</text>
    <text class="fresh" x="268" y="522">Fresh Roasted Coffee</text>
    <text class="scale-word" x="185" y="558">LIGHT</text>
    <ellipse class="roast-bean" cx="226" cy="554" rx="5" ry="7"/><ellipse class="roast-bean" cx="244" cy="554" rx="5" ry="7"/><ellipse class="roast-bean" cx="262" cy="554" rx="5" ry="7"/><ellipse class="roast-bean" cx="280" cy="554" rx="5" ry="7"/><ellipse class="roast-bean-empty" cx="298" cy="554" rx="5" ry="7"/>
    <text class="scale-word" x="342" y="558">DARK</text>
    <text class="ingredients" x="263" y="598">INGREDIENTS COFFEE</text>
    <text class="roast" x="128" y="639">Roast Date :</text>
    <line x1="228" y1="641" x2="403" y2="641" stroke="var(--brown)" stroke-width="1.5"/>
    <text class="weight" x="266" y="676">Net Weight 16 oz (340g)</text>
    <text class="site" x="263" y="725">www.vellorucoffee.example</text>
    <text class="distributor" x="263" y="747">Distributed by Marisol Coffee Roasters, Lindenvale, CA 90000</text>
    <path class="wave-light" d="M138 763q5-6 10 0t10 0t10 0t10 0t10 0t10 0t10 0t10 0t10 0t10 0t10 0t10 0t10 0t10 0t10 0t10 0t10 0t10 0t10 0t10 0t10 0t10 0t10 0t10 0t10 0"/>
  </svg>

  <!-- Brazilian Santos -->
  <svg class="label label--brazilian" viewBox="0 0 526 789" role="img" aria-label="Brazilian Santos label">
    <defs>
      <linearGradient id="bra-left" x1="0" y1="0" x2="0" y2="1">
        <stop offset="0" stop-color="var(--bra-green)"/><stop offset=".6" stop-color="var(--bra-green)"/><stop offset="1" stop-color="var(--bra-yellow)"/>
      </linearGradient>
      <linearGradient id="bra-right" x1="0" y1="0" x2="0" y2="1">
        <stop offset="0" stop-color="var(--bra-yellow)"/><stop offset=".5" stop-color="var(--bra-green)"/><stop offset="1" stop-color="var(--bra-yellow)"/>
      </linearGradient>
    </defs>
    <path class="frame" d="M25 447V98A80 80 0 0 1 105 18H427A80 80 0 0 1 507 98V447"/>
    <text class="brand-name" x="263" y="234">VELLORU</text>
    <rect role="img" aria-label="scattered roasted coffee beans" x="218" y="279" width="90" height="22" rx="11" fill="var(--brown-dark)" opacity=".75"/>
    <rect role="img" aria-label="tiles of Brazilian flag shapes and coffee beans in green and yellow" x="0" y="465" width="90" height="235" fill="url(#bra-left)"/>
    <rect role="img" aria-label="tiles of a coffee bean, a cross and triangles in yellow and green" x="437" y="465" width="89" height="235" fill="url(#bra-right)"/>
    <rect x="0" y="697" width="526" height="92" fill="var(--brown-band)"/>
    <path class="panel" d="M93 697V392H128V370A34 34 0 0 1 162 336H363A34 34 0 0 1 397 370V392H434V697"/>
    <text class="blend-name" x="263" y="384">BRAZILIAN</text>
    <text class="blend-name" x="263" y="426">SANTOS</text>
    <path class="wave" d="M157 456q4-5 8 0t8 0t8 0t8 0t8 0t8 0t8 0t8 0"/>
    <text class="origin" x="263" y="463">ORIGIN</text>
    <path class="wave" d="M308 456q4-5 8 0t8 0t8 0t8 0t8 0t8 0t8 0t8 0"/>
    <text class="arabica" x="268" y="504">100% Arabica</text>
    <text class="fresh" x="268" y="522">Fresh Roasted Coffee</text>
    <text class="scale-word" x="185" y="558">LIGHT</text>
    <ellipse class="roast-bean" cx="226" cy="554" rx="5" ry="7"/><ellipse class="roast-bean" cx="244" cy="554" rx="5" ry="7"/><ellipse class="roast-bean" cx="262" cy="554" rx="5" ry="7"/><ellipse class="roast-bean" cx="280" cy="554" rx="5" ry="7"/><ellipse class="roast-bean-empty" cx="298" cy="554" rx="5" ry="7"/>
    <text class="scale-word" x="342" y="558">DARK</text>
    <text class="ingredients" x="263" y="598">INGREDIENTS COFFEE</text>
    <text class="roast" x="128" y="639">Roast Date :</text>
    <line x1="228" y1="641" x2="403" y2="641" stroke="var(--brown)" stroke-width="1.5"/>
    <text class="weight" x="266" y="676">Net Weight 16 oz (340g)</text>
    <text class="site" x="263" y="725">www.vellorucoffee.example</text>
    <text class="distributor" x="263" y="747">Distributed by Marisol Coffee Roasters, Lindenvale, CA 90000</text>
    <path class="wave-light" d="M138 763q5-6 10 0t10 0t10 0t10 0t10 0t10 0t10 0t10 0t10 0t10 0t10 0t10 0t10 0t10 0t10 0t10 0t10 0t10 0t10 0t10 0t10 0t10 0t10 0t10 0t10 0"/>
  </svg>

  <!-- Gourmet Expresso Blend -->
  <svg class="label label--gourmet" viewBox="0 0 526 789" role="img" aria-label="Gourmet Expresso Blend label">
    <defs>
      <linearGradient id="gou-left" x1="0" y1="0" x2="0" y2="1">
        <stop offset="0" stop-color="var(--gou-tan)"/><stop offset=".45" stop-color="var(--gou-brown)"/><stop offset="1" stop-color="var(--gou-tan)"/>
      </linearGradient>
      <linearGradient id="gou-right" x1="0" y1="0" x2="0" y2="1">
        <stop offset="0" stop-color="var(--gou-brown)"/><stop offset=".45" stop-color="var(--gou-tan)"/><stop offset="1" stop-color="var(--gou-yellow)"/>
      </linearGradient>
    </defs>
    <path class="frame" d="M25 447V98A80 80 0 0 1 105 18H427A80 80 0 0 1 507 98V447"/>
    <text class="brand-name" x="263" y="234">VELLORU</text>
    <rect role="img" aria-label="scattered roasted coffee beans" x="218" y="279" width="90" height="22" rx="11" fill="var(--brown-dark)" opacity=".75"/>
    <rect role="img" aria-label="tiles of a coffee bean, a star and a steaming cup in tan and brown" x="0" y="465" width="90" height="235" fill="url(#gou-left)"/>
    <rect role="img" aria-label="tiles of a flower, a cup and a coffee bean in brown and yellow" x="437" y="465" width="89" height="235" fill="url(#gou-right)"/>
    <rect x="0" y="697" width="526" height="92" fill="var(--brown-band)"/>
    <path class="panel" d="M93 697V392H128V370A34 34 0 0 1 162 336H363A34 34 0 0 1 397 370V392H434V697"/>
    <text class="blend-name" x="263" y="384">GOURMET</text>
    <text class="blend-sub" x="263" y="416">EXPRESSO BLEND</text>
    <path class="wave" d="M157 456q4-5 8 0t8 0t8 0t8 0t8 0t8 0t8 0t8 0"/>
    <text class="origin" x="263" y="463">ORIGIN</text>
    <path class="wave" d="M308 456q4-5 8 0t8 0t8 0t8 0t8 0t8 0t8 0t8 0"/>
    <text class="arabica" x="268" y="504">100% Arabica</text>
    <text class="fresh" x="268" y="522">Fresh Roasted Coffee</text>
    <text class="scale-word" x="185" y="558">LIGHT</text>
    <ellipse class="roast-bean" cx="226" cy="554" rx="5" ry="7"/><ellipse class="roast-bean" cx="244" cy="554" rx="5" ry="7"/><ellipse class="roast-bean" cx="262" cy="554" rx="5" ry="7"/><ellipse class="roast-bean" cx="280" cy="554" rx="5" ry="7"/><ellipse class="roast-bean-empty" cx="298" cy="554" rx="5" ry="7"/>
    <text class="scale-word" x="342" y="558">DARK</text>
    <text class="ingredients" x="263" y="598">INGREDIENTS COFFEE</text>
    <text class="roast" x="128" y="639">Roast Date :</text>
    <line x1="228" y1="641" x2="403" y2="641" stroke="var(--brown)" stroke-width="1.5"/>
    <text class="weight" x="266" y="676">Net Weight 16 oz (340g)</text>
    <text class="site" x="263" y="725">www.vellorucoffee.example</text>
    <text class="distributor" x="263" y="747">Distributed by Marisol Coffee Roasters, Lindenvale, CA 90000</text>
    <path class="wave-light" d="M138 763q5-6 10 0t10 0t10 0t10 0t10 0t10 0t10 0t10 0t10 0t10 0t10 0t10 0t10 0t10 0t10 0t10 0t10 0t10 0t10 0t10 0t10 0t10 0t10 0t10 0t10 0"/>
  </svg>

</main>
</body>
</html>
```